tavremsupply.com

I had a logo designed by pixel forge, and now need a website. I would like all the normal features a website would need.
Payment method etc and I'd like to be able to upload pictures

Target Market(s)

Parents, gift ideas, baby shower, online shopping

Industry/Entity Type

Crowd

Coding

Coded - Design and coding required

Number of Pages Required

1 page

Requirements
Must have
• Would like it to be accessible using a mobile phone
• must be given DNS code so i can add pages as needed
• must be able to upload pictures of products, and up date as needed
Nice to have
• additional pages with no content

```html
<!DOCTYPE html>
<html lang="en">
<head>
<meta charset="utf-8">
<title>Tavrem Supply</title>
<link href="https://fonts.googleapis.com/css2?family=Mulish:wght@300;400;600;700&display=swap" rel="stylesheet">
<style>
:root{
  --ink:#2b2d3a;
  --text:#6f7280;
  --muted:#9a9caa;
  --violet:#8e9bf4;
  --sky:#9fd8ef;
  --rose:#f2b4d2;
  --slate:#b5b8d6;
  --navy:#3e4a8a;
  --panel:#f5f5f6;
  --footer:#5a5e7d;
  --line:#e2e2e8;
}
*{box-sizing:border-box;margin:0;padding:0}
html,body{width:1200px;height:2970px;overflow:hidden}
body{font-family:"Mulish",sans-serif;color:var(--ink);background:#fff;position:relative}
.abs{position:absolute}
a{color:inherit;text-decoration:none}

/* header */
.site-header{position:absolute;left:0;top:0;width:1200px;height:137px;background:#fff}
.brand{position:absolute;left:100px;top:48px;display:flex;align-items:center;gap:12px}
.brand-name{font-size:44px;font-weight:300;color:var(--navy);letter-spacing:1px}
.brand-dot{width:34px;height:34px;border-radius:50%;background:var(--rose)}
.search{position:absolute;left:563px;top:16px;width:273px;height:26px;border:1px solid var(--line);display:flex}
.search span{flex:1;font-size:10px;color:var(--muted);padding:6px 8px}
.search b{width:34px;background:var(--sky);display:flex;align-items:center;justify-content:center}
.account{position:absolute;left:868px;top:21px;display:flex;gap:22px;font-size:11px;letter-spacing:.5px}
.account .reg{color:var(--rose)}
.main-nav{position:absolute;left:433px;top:77px;display:flex;gap:0;font-size:14px;font-weight:600}
.main-nav a{padding:0 22px;height:30px;line-height:18px}
.main-nav .active{color:var(--sky);border-bottom:2px solid var(--sky);padding:0 0 8px;margin:0 22px}

/* hero */
.hero{position:absolute;left:0;top:137px;width:1200px;height:628px;background:linear-gradient(160deg,#cfcdca 0%,#e7e4df 45%,#b8b19f 100%)}
.hero-title{position:absolute;left:0;top:160px;width:1200px;text-align:center;font-size:98px;font-weight:300;color:#fff;letter-spacing:3px}
.hero-sub{position:absolute;left:190px;top:283px;width:820px;text-align:center;font-size:13px;line-height:22px;color:#fff}
.dots{position:absolute;left:557px;top:485px;display:flex;gap:10px}
.dots i{width:14px;height:14px;border-radius:50%;background:#fff;display:block}
.dots i:first-child{background:none;border:2px solid #fff}
.hero-curve{position:absolute;left:0;top:680px}

/* welcome */
.section-title{position:absolute;left:0;width:1200px;text-align:center;font-size:35px;font-weight:400;letter-spacing:1px}
.section-lead{position:absolute;left:180px;width:840px;text-align:center;font-size:13.5px;line-height:27px;color:var(--text)}
.feature{position:absolute;top:915px;width:340px;text-align:center}
.feature .badge{width:160px;height:160px;border-radius:50%;margin:0 auto;border:6px solid #fff;box-shadow:0 0 0 3px currentColor;display:flex;align-items:center;justify-content:center}
.feature h3{margin-top:20px;font-size:23px;font-weight:400;color:var(--ink)}
.feature p{margin-top:10px;font-size:13.5px;line-height:22px;color:var(--muted);padding:0 20px}
.feature .btn{display:inline-block;margin-top:24px;width:152px;height:42px;line-height:40px;border:2px solid currentColor;font-size:16px;font-weight:600}

/* products */
.products{position:absolute;left:0;top:1340px;width:1200px;height:715px;background:var(--panel)}
.pager{position:absolute;left:1045px;top:1508px;display:flex;gap:6px}
.pager span{width:24px;height:24px;border:1px solid #c9c9cf;background:#fff;display:flex;align-items:center;justify-content:center}
.card{position:absolute;top:1560px;width:219px;text-align:center}
.card .photo{height:248px;background:#fff;border:1px solid var(--line);display:flex;align-items:center;justify-content:center}
.card .photo div{width:150px;height:180px;border-radius:12px}
.card h4{margin-top:22px;font-size:14px;font-weight:400;line-height:24px}
.card .price{margin-top:20px;font-size:12px}
.card .price s{color:var(--ink);margin-right:14px}
.card .cart{display:inline-block;margin-top:22px;width:144px;height:38px;line-height:38px;color:#fff;font-size:13px;font-weight:600;letter-spacing:.5px}

/* testimonials */
.quote{position:absolute;left:190px;top:2196px;width:820px;text-align:center;font-size:14px;line-height:27px;color:var(--text)}
.qmark{position:absolute;font-size:70px;color:#e3e3e8;font-family:Georgia,serif;line-height:1}
.avatar{position:absolute;left:530px;top:2335px;width:140px;height:140px;border-radius:50%;border:6px solid #fff;box-shadow:0 0 0 1px var(--line);background:radial-gradient(circle at 45% 40%,#e9d8c6,#9fb0b9 70%)}
.author{position:absolute;left:0;top:2490px;width:1200px;text-align:center;font-size:17px;letter-spacing:2px}

/* footer */
.site-footer{position:absolute;left:0;top:2575px;width:1200px;height:320px;background:var(--footer);color:#fff}
.site-footer .brand{left:100px;top:92px}
.site-footer .brand-name{color:#fff}
.foot-about{position:absolute;left:100px;top:198px;width:310px;font-size:11.5px;line-height:19px}
.foot-rule{position:absolute;top:40px;width:1px;height:240px;background:rgba(255,255,255,.15)}
.foot-head{position:absolute;top:50px;font-size:23px;font-weight:300}
.foot-links{position:absolute;top:105px;list-style:none;font-size:14px;line-height:29px}
.news-form{position:absolute;left:790px;top:95px;width:312px;height:42px;background:#fff;display:flex;align-items:center;padding:0 4px 0 12px}
.news-form span{flex:1;font-size:12px;color:var(--muted);letter-spacing:.5px}
.news-form b{background:var(--footer);font-size:12px;padding:8px 12px;letter-spacing:.5px}
.social{position:absolute;left:790px;top:150px;display:flex;gap:10px}
.social i{width:32px;height:32px;border-radius:50%;background:#fff;display:block}

/* bottom bar */
.legal{position:absolute;left:100px;top:2924px;font-size:12px;color:var(--text)}
.accept{position:absolute;left:855px;top:2918px;display:flex;align-items:center;gap:10px;font-size:12px;color:var(--text)}
.accept i{width:38px;height:24px;border:1px solid var(--line);border-radius:2px;display:block;background:#f0f1f5}
</style>
</head>
<body>

<header class="site-header">
  <a class="brand" href="#"><span class="brand-name">Tavrem</span><span class="brand-dot"></span></a>
  <div class="search"><span>Search entire products here</span>
    <b><svg width="12" height="12" viewBox="0 0 12 12"><circle cx="5" cy="5" r="3.5" fill="none" stroke="#fff" stroke-width="1.5"/><line x1="7.5" y1="7.5" x2="11" y2="11" stroke="#fff" stroke-width="1.5"/></svg></b></div>
  <nav class="account"><a class="reg" href="#">REGISTER</a><a href="#">LOGIN</a><a href="#">&#128722; MY CART(0)</a></nav>
  <nav class="main-nav">
    <a class="active" href="#">HOME</a><a href="#">ABOUT US</a><a href="#">OUR PRODUCTS &#709;</a><a href="#">LATEST NEWS</a><a href="#">CONTACT US</a>
  </nav>
</header>

<section class="hero" role="img" aria-label="Smiling baby crawling on a bed beside soft pillows">
  <h1 class="hero-title">TAVREM SUPPLY</h1>
  <p class="hero-sub">Quis autem vel eum iure reprehenderit qui in ea voluptate velit esse quam nihil molestiae consequatur, vel illum qui dolorem eum fugiat quo voluptas nulla pariatur</p>
  <div class="dots"><i></i><i></i><i></i><i></i></div>
</section>
<svg class="hero-curve" width="1200" height="90" viewBox="0 0 1200 90"><path d="M0 90 Q600 -40 1200 90 Z" fill="#fff"/></svg>

<h2 class="section-title" style="top:757px">WELCOME TO TAVREM</h2>
<p class="section-lead" style="top:814px">Neque porro quisquam est, qui dolorem ipsum quia dolor sit amet, consectetur, adipisci velit, sed quia non numquam eius modi tempora incidunt ut labore et dolore magnam aliquam quaerat voluptatem</p>

<div class="feature" style="left:80px;color:var(--violet)">
  <div class="badge" style="background:var(--violet)"><svg width="70" height="70" viewBox="0 0 70 70"><circle cx="35" cy="35" r="24" fill="none" stroke="#fff" stroke-width="4"/><text x="35" y="46" text-anchor="middle" font-size="32" font-family="Mulish,sans-serif" font-weight="700" fill="#fff">$</text></svg></div>
  <h3>BEST COLLECTION</h3>
  <p>Nemo enim ipsam voluptatem quia voluptas sit aspernatur aut odit aut fugit, sed quia consequuntur magni dolores.</p>
  <a class="btn" href="#">LEARN MORE</a>
</div>
<div class="feature" style="left:430px;color:var(--sky)">
  <div class="badge" style="background:var(--sky)"><svg width="80" height="60" viewBox="0 0 80 60"><rect x="4" y="12" width="44" height="30" rx="3" fill="#fff"/><path d="M50 20h14l10 12v10H50z" fill="#fff"/><circle cx="18" cy="46" r="7" fill="#fff" stroke="var(--sky)" stroke-width="3"/><circle cx="62" cy="46" r="7" fill="#fff" stroke="var(--sky)" stroke-width="3"/></svg></div>
  <h3>FAST DELIVERY</h3>
  <p>Nemo enim ipsam voluptatem quia voluptas sit aspernatur aut odit aut fugit, sed quia consequuntur magni dolores.</p>
  <a class="btn" href="#">LEARN MORE</a>
</div>
<div class="feature" style="left:785px;color:var(--rose)">
  <div class="badge" style="background:var(--rose)"><svg width="70" height="70" viewBox="0 0 70 70"><circle cx="35" cy="35" r="24" fill="none" stroke="#fff" stroke-width="4"/><path d="M23 36l8 8 16-18" fill="none" stroke="#fff" stroke-width="5" stroke-linecap="round" stroke-linejoin="round"/></svg></div>
  <h3>BEST QUALITY</h3>
  <p>Nemo enim ipsam voluptatem quia voluptas sit aspernatur aut odit aut fugit, sed quia consequuntur magni dolores.</p>
  <a class="btn" href="#">LEARN MORE</a>
</div>

<section class="products"></section>
<h2 class="section-title" style="top:1400px">TAVREM PRODUCTS</h2>
<p class="section-lead" style="top:1456px;left:170px;width:860px">But I must explain to you how all this mistaken idea of denouncing pleasure and praising pain was born and I will give you a complete account of the system.</p>
<div class="pager"><span><svg width="8" height="10" viewBox="0 0 8 10"><path d="M6 1L2 5l4 4" fill="none" stroke="#666" stroke-width="1.5"/></svg></span><span><svg width="8" height="10" viewBox="0 0 8 10"><path d="M2 1l4 4-4 4" fill="none" stroke="#666" stroke-width="1.5"/></svg></span></div>

<article class="card" style="left:100px">
  <div class="photo"><div role="img" aria-label="Cloud-shaped hanging baby rattle toy" style="background:linear-gradient(160deg,#f3f3f3,#c9cbd2 60%,#f0c36a)"></div></div>
  <h4>Quis Nostrud Exercitation<br>Ullamco Laboris</h4>
  <p class="price"><s>$13.99-$45.99</s><span style="color:var(--violet)">$5.99-$43.99</span></p>
  <a class="cart" href="#" style="background:var(--violet)">ADD TO CART</a>
</article>
<article class="card" style="left:360px">
  <div class="photo"><div role="img" aria-label="Stainless steel baby bottle with spare teat" style="background:linear-gradient(90deg,#9c9fa5,#e6e7ea 45%,#8d9096);width:80px"></div></div>
  <h4>Nisi Ut Aliquip Ex Commodo<br>Consequat Irure</h4>
  <p class="price"><s>$20.99-$30.99</s><span style="color:var(--sky)">$7.99-$14.99</span></p>
  <a class="cart" href="#" style="background:var(--sky)">ADD TO CART</a>
</article>
<article class="card" style="left:620px">
  <div class="photo"><div role="img" aria-label="Folded baby blanket in a woven gift basket" style="background:linear-gradient(170deg,#efe6d2,#f7f3ec 50%,#d9cdb5);height:110px"></div></div>
  <h4>Voluptatem Accusantium<br>Dolorem Laudantium</h4>
  <p class="price"><s>$19.99</s><span style="color:var(--rose)">$16.99</span></p>
  <a class="cart" href="#" style="background:var(--rose)">ADD TO CART</a>
</article>
<article class="card" style="left:881px">
  <div class="photo"><div role="img" aria-label="White baby bathtub with running faucet" style="background:linear-gradient(180deg,#f4f5f6,#dfe3e6 60%,#9fd4ec);height:130px;width:170px"></div></div>
  <h4>Eaque Ipsa Quae Ab Illo<br>Inventore Veritatis</h4>
  <p class="price"><s>$105.00</s><span style="color:var(--slate)">$35.00</span></p>
  <a class="cart" href="#" style="background:var(--slate)">ADD TO CART</a>
</article>

<h2 class="section-title" style="top:2128px">CLIENT TESTIMONIALS</h2>
<svg class="abs" style="left:96px;top:2252px" width="20" height="40" viewBox="0 0 20 40"><path d="M18 2L2 20l16 18" fill="none" stroke="#e3e3e8" stroke-width="2"/></svg>
<svg class="abs" style="left:1084px;top:2252px" width="20" height="40" viewBox="0 0 20 40"><path d="M2 2l16 18L2 38" fill="none" stroke="#e3e3e8" stroke-width="2"/></svg>
<span class="qmark" style="left:140px;top:2185px">&ldquo;</span>
<span class="qmark" style="left:1005px;top:2285px">&rdquo;</span>
<p class="quote">But I must explain to you how all this mistaken idea of denouncing pleasure and praising pain was born and I will give you a complete account of the system, and expound the actual teachings of the great explorer of the truth, the master-builder of human happiness. No one rejects, dislikes, or avoids pleasure itself, because it is pleasure, but because those who do not know how to pursue pleasure rationally encounter consequences that are extremely painful</p>
<div class="avatar" role="img" aria-label="Portrait of a client with a stroller outdoors"></div>
<p class="author">- ASSUMENDA EST</p>

<footer class="site-footer">
  <a class="brand" href="#"><span class="brand-name">Tavrem</span><span class="brand-dot"></span></a>
  <p class="foot-about">But I must explain to you how all this mistaken idea of denouncing pleasure and praising pain was born and I will give you a complete account of the system.</p>
  <span class="foot-rule" style="left:413px"></span>
  <span class="foot-rule" style="left:765px"></span>
  <h3 class="foot-head" style="left:440px">Quick Links</h3>
  <ul class="foot-links" style="left:440px"><li>Home</li><li>About Us</li><li>Our Products</li><li>Latest News</li><li>Contact Us</li></ul>
  <ul class="foot-links" style="left:612px"><li>Terms &amp; Conditions</li><li>Privacy Policy</li><li>Blog</li><li>FAQ</li></ul>
  <h3 class="foot-head" style="left:790px">Join Newsletters</h3>
  <div class="news-form"><span>EMAIL ADDRESS</span><b>SUBSCRIBE</b></div>
  <div class="social"><i></i><i></i><i></i><i></i><i></i></div>
</footer>

<p class="legal">&copy; 2017 Tavrem. &nbsp;All right reserved. &nbsp;Term of Use</p>
<div class="accept">We Accept: <span style="width:8px"></span><i></i><i></i><i></i><i></i></div>

</body>
</html>
```